Need a Modern, Professional Website Design for Life Coaching Company in United States

Need Life Coaching Website Design for Life Coaching Company in the United States to wow and attract clients. Need a modern professional website to land clients.
- I am looking for an inspirational-looking website. Most of my clients will be female, but I want to attract both male and female clients, but I want to more females, site should be more feminine that masculine but attract both.

Target Market(s)

Adult women and men age 30 - 58

Colors
0054AA
0677BA
7BADD7
CADEEF
E8F1F8

Requirements
Must have
• modern, professional feel

```html
<!DOCTYPE html>
<html lang="en">
<head>
<meta charset="utf-8">
<title>Brightpath Coaching – Homepage Concepts</title>
<link href="https://fonts.googleapis.com/css2?family=Poppins:wght@400;500;600&family=Roboto:wght@400;500;700&display=swap" rel="stylesheet">
<style>
:root{
  --blue:#0054aa;
  --blue-2:#0677ba;
  --blue-3:#7badd7;
  --blue-4:#cadeef;
  --tint:#e8f1f8;
  --ink:#2a2a2a;
  --body:#6b6b6b;
  --dark:#2b2b2b;
  --stage:#f4f2f3;
  --white:#ffffff;
}
*{box-sizing:border-box;margin:0;padding:0}
html,body{width:1200px;height:2326px;overflow:hidden}
body{background:var(--stage);font-family:"Roboto",Arial,sans-serif;color:var(--ink)}
.page{position:absolute;top:82px;width:526px;background:var(--white);transform:scale(.9029);transform-origin:0 0;box-shadow:0 6px 24px rgba(0,0,0,.12);overflow:hidden}
.page--a{left:95px}
.page--b{left:644px}
section,header,footer{position:relative;overflow:hidden}

/* header */
.site-header{height:52px;display:grid;grid-template-columns:1fr auto 1fr;align-items:center;padding:0 48px}
.nav{display:flex;gap:10px;font-size:5px;font-weight:700;text-transform:uppercase;letter-spacing:.1px}
.nav a{color:var(--ink);text-decoration:none}
.nav a.is-active{color:var(--blue)}
.brand{text-align:center;font-family:"Poppins",sans-serif;font-weight:600;color:var(--blue);line-height:1}
.brand__name{font-size:15px;letter-spacing:.6px;display:block}
.brand__sub{font-size:8px;letter-spacing:.6px;display:block;margin-top:1px}
.header-right{display:flex;justify-content:flex-end;align-items:center;gap:14px;font-size:5px;font-weight:700}
.socials{display:flex;gap:5px}
.socials span{width:12px;height:12px;border-radius:50%;border:1px solid #d5d5d5;display:block}
.socials span:first-child{background:var(--blue);border-color:var(--blue)}

/* hero */
.hero{position:relative}
.hero__photo{position:absolute;inset:0}
.hero__text{position:absolute;font-family:"Poppins",sans-serif;font-weight:500;font-size:10.6px;line-height:17.3px;color:var(--ink);width:205px}
.hero__text b{color:var(--blue);font-weight:600}
.arrow{position:absolute;width:13px;height:13px;border-radius:50%;background:var(--white);display:flex;align-items:center;justify-content:center;box-shadow:0 1px 3px rgba(0,0,0,.2)}
.arrow--ghost{background:#d6d6d6;box-shadow:none}
.arrow svg{width:5px;height:5px}

/* headings */
.title{font-family:"Poppins",sans-serif;font-weight:500;font-size:15px;line-height:20px;color:var(--ink);text-align:center}
.title::after{content:"";display:block;width:22px;height:2px;background:var(--blue);margin:4px auto 0}
.title--left{text-align:left}
.title--left::after{margin-left:0}
.title--light{color:var(--white);font-size:12.5px;line-height:17px}
.title--light::after{background:var(--white);margin-left:0}

/* services */
.cards{position:absolute;left:0;right:0;display:flex;justify-content:center;gap:10.5px}
.svc{width:100px;height:102px;background:var(--white);box-shadow:0 2px 8px rgba(0,0,0,.12);display:flex;flex-direction:column;align-items:center;padding-top:17px}
.svc--active{background:var(--blue)}
.icon{width:37px;height:37px;border-radius:50%;background:var(--blue);display:flex;align-items:center;justify-content:center}
.svc--active .icon{background:var(--white)}
.icon svg{width:20px;height:20px;fill:none;stroke:var(--white);stroke-width:1.6;stroke-linecap:round;stroke-linejoin:round}
.svc--active .icon svg{stroke:var(--blue)}
.svc__label{margin-top:10px;font-size:6px;font-weight:500;line-height:10.5px;text-align:center;text-transform:uppercase;color:var(--ink)}
.svc--active .svc__label{color:var(--white)}

/* about */
.about{background:var(--tint)}
.photo-box{position:absolute;left:48px;width:215px;height:173px;border-radius:10px;box-shadow:0 2px 6px rgba(0,0,0,.15)}
.about__copy{position:absolute;left:298px;width:180px}
.para{font-size:5.1px;line-height:9.3px;color:var(--body);text-align:justify;margin-top:12px}
.btn{display:inline-block;background:var(--blue);color:var(--white);font-size:4.6px;font-weight:700;text-transform:uppercase;border-radius:9px;padding:6px 12px}

/* how it works */
.how__text{position:absolute;left:58px;right:58px;font-size:5.2px;line-height:9.3px;color:var(--body);text-align:center}
.how__text p+p{margin-top:8px}
.step{width:100px;height:138px;background:var(--white);box-shadow:0 2px 8px rgba(0,0,0,.12);display:flex;flex-direction:column;align-items:center;padding:14px 7px 0}
.step .icon{width:31px;height:31px}
.step .icon svg{width:17px;height:17px}
.step__title{margin-top:9px;font-size:6px;font-weight:700;line-height:10px;text-align:center;text-transform:uppercase}
.step__dot{width:3px;height:3px;border-radius:50%;background:#c4c4c4;margin:3px 0 4px}
.step__text{font-size:4.6px;line-height:8.4px;color:var(--body);text-align:center}

/* benefits */
.benefits{background:linear-gradient(115deg,#0a3f86 0%,#0054aa 45%,#0a4d9c 70%,#123c78 100%);color:var(--white)}
.benefits__list{position:absolute;left:48px;list-style:none;font-size:5.2px;line-height:13.5px}
.benefits__list li{position:relative;padding-left:19px}
.benefits__list li::before{content:"";position:absolute;left:0;top:4.5px;width:5px;height:5px;border-radius:50%;background:var(--white);box-shadow:inset 0 0 0 1.5px var(--white)}
.round-photo{position:absolute;border-radius:50%;border:4px solid var(--white)}

/* about me */
.ring{position:absolute;width:190px;height:190px;border-radius:50%;background:var(--blue)}
.ring__photo{position:absolute;left:6px;top:2px;width:184px;height:186px;border-radius:50%}
.me__copy{position:absolute;left:269px;width:210px}
.me__line{font-size:5.4px;color:var(--ink);margin-top:9px}
.me__sign{font-size:5.4px;color:var(--blue);font-weight:700;margin-top:5px}

/* quotes */
.quotes{background:var(--tint)}
.avatar{position:absolute;left:50%;width:24px;height:24px;margin-left:-12px;border-radius:50%}
.avatar__badge{position:absolute;right:-3px;top:-2px;width:8px;height:8px;border-radius:50%;background:var(--blue);border:1px solid var(--white)}
.quote__text{position:absolute;left:0;right:0;text-align:center;font-size:6.5px;color:var(--body)}
.quote__by{position:absolute;left:0;right:0;text-align:center;font-size:5px;font-style:italic;font-weight:500;color:var(--blue)}

/* contact form */
.start__text{position:absolute;left:70px;right:70px;text-align:center;font-size:5.3px;line-height:9.7px;color:var(--body)}
.form{position:absolute;left:107px;width:311px}
.form__row{display:flex;gap:6px}
.field{background:var(--white);border:1px solid #e3e3e3;box-shadow:0 1px 3px rgba(0,0,0,.06);font-size:5px;color:#777;padding:6px 7px;height:20px;flex:1}
.field--area{height:41px;margin-top:6px}
.form__submit{display:block;width:52px;margin:6px auto 0;text-align:center;padding:5px 0}

/* footer */
.site-footer{color:var(--white);text-align:center}
.footer__body{position:absolute;left:0;right:0;bottom:0;background:var(--dark)}
.footer__brand{font-family:"Poppins",sans-serif;font-weight:600;color:var(--white);line-height:1}
.footer__brand .brand__name{font-size:14px}
.footer__brand .brand__sub{font-size:7.5px}
.footer__nav{font-size:5.2px;font-weight:700;text-transform:uppercase;display:flex;justify-content:center;gap:9px;margin-top:12px}
.footer__nav i{font-style:normal;color:#bbb}
.footer__contact{font-size:5.2px;margin-top:7px;display:flex;justify-content:center;gap:8px;align-items:center}
.footer__contact svg{width:5px;height:5px;fill:var(--blue-3);vertical-align:-1px;margin-right:3px}
.footer__social{display:flex;justify-content:center;gap:3px;margin-top:7px}
.footer__social span{width:10px;height:10px;border-radius:50%;background:var(--white)}
.footer__social span:first-child{background:var(--blue)}
.footer__rule{height:1px;background:#444;margin:10px 48px 0}
.footer__copy{font-size:4.3px;margin-top:8px}
</style>
</head>
<body>

<!-- ===================== CONCEPT A ===================== -->
<div class="page page--a">
  <header class="site-header">
    <nav class="nav"><a class="is-active">Home</a><a>Services</a><a>Courses</a><a>About</a></nav>
    <div class="brand"><span class="brand__name">BRIGHTPATH</span><span class="brand__sub">COACHING</span></div>
    <div class="header-right"><span>CONTACT</span><div class="socials"><span></span><span></span><span></span><span></span></div></div>
  </header>

  <section class="hero" style="height:283px">
    <div class="hero__photo" role="img" aria-label="Woman with curly hair, eyes closed, hands pressed together in thought, in warm window light" style="background:linear-gradient(90deg,#a3602a 0%,#c98748 22%,#e7c9a2 45%,#f3e4d0 62%,#efe6de 100%)"></div>
    <svg style="position:absolute;left:0;top:0" width="526" height="283" viewBox="0 0 526 283">
      <path d="M0,238 C70,282 170,296 290,268 C380,247 450,220 526,268 L526,283 L0,283 Z" fill="#fff"/>
      <path d="M0,240 C70,286 170,300 290,272 C380,251 450,222 526,272" fill="none" stroke="#0054aa" stroke-width="5"/>
    </svg>
    <p class="hero__text" style="left:281px;top:86px">Do you feel stuck or stagnant in reaching your goals? Gain clarity, confidence, accountability, and support from <b>BRIGHTPATH</b> and <b>ACHIEVE SUCCESS!</b></p>
    <span class="arrow" style="left:18px;top:120px"><svg viewBox="0 0 6 6"><path d="M4,0.5 L1.5,3 L4,5.5" fill="none" stroke="#333" stroke-width="1"/></svg></span>
    <span class="arrow" style="left:495px;top:120px"><svg viewBox="0 0 6 6"><path d="M2,0.5 L4.5,3 L2,5.5" fill="none" stroke="#333" stroke-width="1"/></svg></span>
  </section>

  <section style="height:237px">
    <h2 class="title" style="position:absolute;left:0;right:0;top:30px">Coaching Services to Help You<br>Pivot and Prosper</h2>
    <div class="cards" style="top:93px">
      <div class="svc"><span class="icon"><svg viewBox="0 0 20 20"><rect x="3" y="7" width="14" height="9" rx="1"/><path d="M7,7 V5 H13 V7 M3,11 H17"/></svg></span><span class="svc__label">Career<br>Coaching</span></div>
      <div class="svc"><span class="icon"><svg viewBox="0 0 20 20"><circle cx="10" cy="10" r="6.5"/><path d="M10,6 V10 L13,12"/></svg></span><span class="svc__label">Life Reset<br>Coaching</span></div>
      <div class="svc svc--active"><span class="icon"><svg viewBox="0 0 20 20"><path d="M6,16 V12 C4,10 4,5 9,4 C14,3 16,7 15,10 L16,12 H14.5 V15 H11 V16"/><circle cx="10" cy="8.5" r="2"/></svg></span><span class="svc__label">Mindset<br>Coaching</span></div>
      <div class="svc"><span class="icon"><svg viewBox="0 0 20 20"><circle cx="10" cy="9" r="3"/><path d="M10,3 V5 M10,13 V15 M4,9 H6 M14,9 H16 M5.8,4.8 L7.2,6.2 M12.8,11.8 L14.2,13.2 M5.8,13.2 L7.2,11.8 M12.8,6.2 L14.2,4.8 M5,17 H15"/></svg></span><span class="svc__label">Resilience<br>Coaching</span></div>
    </div>
    <span class="arrow arrow--ghost" style="left:16px;top:160px"><svg viewBox="0 0 6 6"><path d="M4,0.5 L1.5,3 L4,5.5" fill="none" stroke="#fff" stroke-width="1"/></svg></span>
    <span class="arrow arrow--ghost" style="left:496px;top:160px"><svg viewBox="0 0 6 6"><path d="M2,0.5 L4.5,3 L2,5.5" fill="none" stroke="#fff" stroke-width="1"/></svg></span>
  </section>

  <section class="about" style="height:248px">
    <div class="photo-box" style="top:37px;background:linear-gradient(100deg,#e8e6e2 0%,#b9b4ad 40%,#6f7b8c 62%,#d9dadb 100%)" role="img" aria-label="Man with glasses and headset working at a laptop in a home office"></div>
    <div class="about__copy" style="top:50px">
      <h2 class="title title--left">About Us</h2>
      <p class="para">Brightpath Coaching offers coaching services for adult women and men willing and ready to work hard to create the life they crave. Whether you want to increase your confidence, discover your life's purpose, land your dream job, or improve your relationships, we would be happy to help you reach your goals.</p>
      <span class="btn" style="margin-top:12px">Read More</span>
    </div>
  </section>

  <section style="height:422px">
    <h2 class="title" style="position:absolute;left:0;right:0;top:44px">How Coaching Works</h2>
    <div class="how__text" style="top:88px">
      <p>You can choose a 30 or 60-minute phone or video session. Brightpath Coaching offers a 90-Day Jump Start Coaching Program to help you set goals and take action. Individual coaching sessions range in price from $50.00 to $75.00. Deep down, you know you desire success. So, get started today! Get the life you crave!</p>
      <p>Like an athletic coach, a life coach comes alongside you to encourage, equip, and empower you to succeed. Your life coach will work with you to discover your passion, set realistic goals, create plans, and take action. Through goal-setting strategies, transformational coaching, and accountability, you will have a firm foundation to help you live a purposeful, abundant life.</p>
      <p>Life coaching is not a form of counseling. Counseling delves into your past behaviors and patterns. But life coaching is a future-oriented process – helping you close the gap between where you are now and where you desire to be. Life coaching focuses on your strengths and positive outlook. Life coaching is about goal setting for an already emotionally and mentally healthy person. Life coaching is not consulting; you do the self-development work for yourself.</p>
    </div>
    <div class="cards" style="top:232px">
      <div class="step"><span class="icon"><svg viewBox="0 0 20 20"><circle cx="10" cy="7" r="3"/><path d="M4,17 C4,13 16,13 16,17 M7,5 C7,2 13,2 13,5"/></svg></span><span class="step__title">Discovery Call</span><span class="step__dot"></span><span class="step__text">Lorem ipsum dolor sit amet, con sectetur adipiscing elit, sed do eiusmod tempor incididunt ut labore et dolorea.</span></div>
      <div class="step"><span class="icon"><svg viewBox="0 0 20 20"><circle cx="10" cy="10" r="7"/><circle cx="10" cy="9" r="2.5"/><path d="M5.5,15 C7,12 13,12 14.5,15 M15,3 V7 M13,5 H17"/></svg></span><span class="step__title">Sign Up</span><span class="step__dot"></span><span class="step__text">Lorem ipsum dolor sit amet, con sectetur adipiscing elit, sed do eiusmod tempor incididunt ut labore et dolorea.</span></div>
      <div class="step"><span class="icon"><svg viewBox="0 0 20 20"><rect x="5" y="3" width="10" height="14" rx="1"/><path d="M7.5,7 H12.5 M7.5,10 H12.5 M7.5,13 H10.5"/></svg></span><span class="step__title">Pre-Coaching<br>Questionnaire</span><span class="step__dot"></span><span class="step__text">Lorem ipsum dolor sit amet, con sectetur adipiscing elit, sed do eiusmod temporea.</span></div>
      <div class="step"><span class="icon"><svg viewBox="0 0 20 20"><rect x="3" y="3" width="14" height="8" rx="1"/><circle cx="6" cy="14" r="1.5"/><circle cx="10" cy="14" r="1.5"/><circle cx="14" cy="14" r="1.5"/><path d="M6,7 H14"/></svg></span><span class="step__title">1:1 Coaching<br>Session</span><span class="step__dot"></span><span class="step__text">Lorem ipsum dolor sit amet, con sectetur adipiscing elit, sed do eiusmod temporea.</span></div>
    </div>
  </section>

  <section class="benefits" style="height:248px">
    <h2 class="title title--light" style="position:absolute;left:48px;top:31px;text-align:left">Benefits of Life Coaching<br>Include</h2>
    <ul class="benefits__list" style="top:80px">
      <li>Accountability and support to help you succeed</li><li>Overcome obstacles</li><li>Gain clarity about what you want</li><li>Thrive from your God-given purpose</li><li>Happiness from pursuing and reaching goals</li><li>Encouragement and guidance to help you stay on track</li><li>Strategies to help you reach goals faster</li><li>Energy from doing what excites</li><li>Joy from doing what you love</li><li>Increase productivity</li>
    </ul>
    <div class="round-photo" style="left:287px;top:29px;width:190px;height:190px;background:linear-gradient(120deg,#e9d6b6 0%,#d7a45f 45%,#b8651e 70%,#4b6a86 100%)" role="img" aria-label="Woman in an orange sweater with arms spread wide at sunset by the sea"></div>
  </section>

  <section style="height:283px">
    <div class="ring" style="left:48px;top:46px"><div class="ring__photo" role="img" aria-label="Portrait of the coach smiling, wearing glasses" style="background:linear-gradient(160deg,#f1f3f5 0%,#d9dce0 55%,#8a8f96 100%)"></div></div>
    <div class="me__copy" style="top:59px">
      <h2 class="title title--left">About Me</h2>
      <p class="para">Hi. I am Dana Whitfield. I'm a life and career coach. I'm so excited that you are here, ready to take control of your destiny. Like you, I've experienced my share of life's ups, downs, twists, and turns. To overcome those challenges, I remained committed, resilient, and optimistic about my goals and lifelong learning. Most importantly, I couldn't give up because too much was at stake. I had to keep going. So, I am asking you, are you ready to move forward to live beyond your wildest dreams? If so, I invite you to contact me today to learn more.</p>
      <p class="me__line">Let's partner together and co-create your desired future</p>
      <p class="me__sign">Cheers! Dana</p>
    </div>
  </section>

  <section class="quotes" style="height:162px">
    <h2 class="title" style="position:absolute;left:0;right:0;top:21px">Inspirational Quotes</h2>
    <div class="avatar" style="top:73px;background:linear-gradient(160deg,#eceae8,#b9b0a6)" role="img" aria-label="Small round author portrait"><span class="avatar__badge"></span></div>
    <span class="arrow arrow--ghost" style="left:48px;top:97px"><svg viewBox="0 0 6 6"><path d="M4,0.5 L1.5,3 L4,5.5" fill="none" stroke="#fff" stroke-width="1"/></svg></span>
    <span class="arrow arrow--ghost" style="left:462px;top:97px"><svg viewBox="0 0 6 6"><path d="M2,0.5 L4.5,3 L2,5.5" fill="none" stroke="#fff" stroke-width="1"/></svg></span>
    <p class="quote__text" style="top:119px">When you are going through hell, keep going!</p>
    <p class="quote__by" style="top:134px">Marcus Hale</p>
  </section>

  <section style="height:250px">
    <h2 class="title" style="position:absolute;left:0;right:0;top:39px">Get Started Today</h2>
    <p class="start__text" style="top:80px">Request a free 15-minute phone consultation to see how we can help you achieve your goals. Step boldly into your greatness.<br>Contact us today to start living a happier, more fulfilled, meaningful life.</p>
    <div class="form" style="top:117px">
      <div class="form__row"><div class="field">Name</div><div class="field">Email</div></div>
      <div class="field field--area">Comments</div>
      <span class="btn form__submit">Submit</span>
    </div>
  </section>

  <footer class="site-footer" style="height:209px">
    <svg style="position:absolute;left:0;top:0" width="526" height="60" viewBox="0 0 526 60">
      <path d="M0,14 C90,48 200,58 300,40 C390,24 460,8 526,40 L526,60 L0,60 Z" fill="#2b2b2b"/>
      <path d="M0,8 C90,42 200,52 300,34 C390,18 460,2 526,34" fill="none" stroke="#0054aa" stroke-width="5"/>
    </svg>
    <div class="footer__body" style="top:59px;padding-top:9px">
      <div class="footer__brand"><span class="brand__name">BRIGHTPATH</span><span class="brand__sub">COACHING</span></div>
      <div class="footer__nav"><span>Home</span><i>|</i><span>Coaching Services</span><i>|</i><span>About Us</span><i>|</i><span>Courses</span><i>|</i><span>Contact Us</span></div>
      <div class="footer__contact"><span><svg viewBox="0 0 10 10"><path d="M2,1 L4,1 L5,3.5 L3.8,4.5 C4.5,6 5,6.5 6,6.8 L7,5.5 L9,6.5 L9,8.5 C5,9 1,5 2,1 Z"/></svg>555-014-2290</span><span>|</span><span><svg viewBox="0 0 10 10"><path d="M5,0.5 C7.5,0.5 8.5,2.5 8,4.5 L5,9.5 L2,4.5 C1.5,2.5 2.5,0.5 5,0.5 Z"/></svg>Located in Fairview, NC</span></div>
      <div class="footer__contact" style="margin-top:4px"><span><svg viewBox="0 0 10 10"><rect x="0.5" y="2" width="9" height="6"/></svg>hello@brightpathcoaching.com</span></div>
      <div class="footer__social"><span></span><span></span><span></span><span></span></div>
      <div class="footer__rule"></div>
      <p class="footer__copy">© 2023 <b>BRIGHTPATH COACHING</b> &nbsp;|&nbsp; All Rights Reserved</p>
    </div>
  </footer>
</div>

<!-- ===================== CONCEPT B ===================== -->
<div class="page page--b">
  <header class="site-header">
    <nav class="nav"><a class="is-active">Home</a><a>Services</a><a>Courses</a><a>About</a></nav>
    <div class="brand"><span class="brand__name">BRIGHTPATH</span><span class="brand__sub">COACHING</span></div>
    <div class="header-right"><span>CONTACT</span><div class="socials"><span></span><span></span><span></span><span></span></div></div>
  </header>

  <section class="hero" style="height:252px">
    <div class="hero__photo" role="img" aria-label="Woman in an orange sweater with arms spread wide, facing a sunlit sea" style="background:linear-gradient(90deg,#f1e2c2 0%,#e9c989 35%,#dca55a 60%,#c07a2a 75%,#e2c08a 100%)"></div>
    <p class="hero__text" style="left:49px;top:84px;width:170px"><b>Brightpath Coaching</b> offers coaching services for adult women and men willing and ready to work hard to create the life they crave.</p>
    <span class="arrow" style="left:18px;top:119px"><svg viewBox="0 0 6 6"><path d="M4,0.5 L1.5,3 L4,5.5" fill="none" stroke="#333" stroke-width="1"/></svg></span>
    <span class="arrow" style="left:495px;top:119px"><svg viewBox="0 0 6 6"><path d="M2,0.5 L4.5,3 L2,5.5" fill="none" stroke="#333" stroke-width="1"/></svg></span>
  </section>

  <section style="height:243px">
    <h2 class="title" style="position:absolute;left:0;right:0;top:41px">Coaching Services to Help You<br>Pivot and Prosper</h2>
    <div class="cards" style="top:105px">
      <div class="svc"><span class="icon"><svg viewBox="0 0 20 20"><rect x="3" y="7" width="14" height="9" rx="1"/><path d="M7,7 V5 H13 V7 M3,11 H17"/></svg></span><span class="svc__label">Career<br>Coaching</span></div>
      <div class="svc"><span class="icon"><svg viewBox="0 0 20 20"><circle cx="10" cy="10" r="6.5"/><path d="M10,6 V10 L13,12"/></svg></span><span class="svc__label">Life Reset<br>Coaching</span></div>
      <div class="svc svc--active"><span class="icon"><svg viewBox="0 0 20 20"><path d="M6,16 V12 C4,10 4,5 9,4 C14,3 16,7 15,10 L16,12 H14.5 V15 H11 V16"/><circle cx="10" cy="8.5" r="2"/></svg></span><span class="svc__label">Mindset<br>Coaching</span></div>
      <div class="svc"><span class="icon"><svg viewBox="0 0 20 20"><circle cx="10" cy="9" r="3"/><path d="M10,3 V5 M10,13 V15 M4,9 H6 M14,9 H16 M5.8,4.8 L7.2,6.2 M12.8,11.8 L14.2,13.2 M5.8,13.2 L7.2,11.8 M12.8,6.2 L14.2,4.8 M5,17 H15"/></svg></span><span class="svc__label">Resilience<br>Coaching</span></div>
    </div>
    <span class="arrow arrow--ghost" style="left:16px;top:150px"><svg viewBox="0 0 6 6"><path d="M4,0.5 L1.5,3 L4,5.5" fill="none" stroke="#fff" stroke-width="1"/></svg></span>
    <span class="arrow arrow--ghost" style="left:496px;top:150px"><svg viewBox="0 0 6 6"><path d="M2,0.5 L4.5,3 L2,5.5" fill="none" stroke="#fff" stroke-width="1"/></svg></span>
  </section>

  <section class="about" style="height:248px">
    <div class="photo-box" style="top:38px;background:linear-gradient(100deg,#e8e6e2 0%,#b9b4ad 40%,#6f7b8c 62%,#d9dadb 100%)" role="img" aria-label="Man with glasses and headset working at a laptop in a home office"></div>
    <div class="about__copy" style="top:51px">
      <h2 class="title title--left">About Us</h2>
      <p class="para">Brightpath Coaching offers coaching services for adult women and men willing and ready to work hard to create the life they crave. Whether you want to increase your confidence, discover your life's purpose, land your dream job, or improve your relationships, we would be happy to help you reach your goals.</p>
      <span class="btn" style="margin-top:12px">Read More</span>
    </div>
  </section>

  <section style="height:422px">
    <h2 class="title" style="position:absolute;left:0;right:0;top:45px">How Coaching Works</h2>
    <div class="how__text" style="top:88px">
      <p>You can choose a 30 or 60-minute phone or video session. Brightpath Coaching offers a 90-Day Jump Start Coaching Program to help you set goals and take action. Individual coaching sessions range in price from $50.00 to $75.00. Deep down, you know you desire success. So, get started today! Get the life you crave!</p>
      <p>Like an athletic coach, a life coach comes alongside you to encourage, equip, and empower you to succeed. Your life coach will work with you to discover your passion, set realistic goals, create plans, and take action. Through goal-setting strategies, transformational coaching, and accountability, you will have a firm foundation to help you live a purposeful, abundant life.</p>
      <p>Life coaching is not a form of counseling. Counseling delves into your past behaviors and patterns. But life coaching is a future-oriented process – helping you close the gap between where you are now and where you desire to be. Life coaching focuses on your strengths and positive outlook. Life coaching is about goal setting for an already emotionally and mentally healthy person. Life coaching is not consulting; you do the self-development work for yourself.</p>
    </div>
    <div class="cards" style="top:234px">
      <div class="step"><span class="icon"><svg viewBox="0 0 20 20"><circle cx="10" cy="7" r="3"/><path d="M4,17 C4,13 16,13 16,17 M7,5 C7,2 13,2 13,5"/></svg></span><span class="step__title">Discovery Call</span><span class="step__dot"></span><span class="step__text">Lorem ipsum dolor sit amet, con sectetur adipiscing elit, sed do eiusmod tempor incididunt ut labore et dolorea.</span></div>
      <div class="step"><span class="icon"><svg viewBox="0 0 20 20"><circle cx="10" cy="10" r="7"/><circle cx="10" cy="9" r="2.5"/><path d="M5.5,15 C7,12 13,12 14.5,15 M15,3 V7 M13,5 H17"/></svg></span><span class="step__title">Sign Up</span><span class="step__dot"></span><span class="step__text">Lorem ipsum dolor sit amet, con sectetur adipiscing elit, sed do eiusmod tempor incididunt ut labore et dolorea.</span></div>
      <div class="step"><span class="icon"><svg viewBox="0 0 20 20"><rect x="5" y="3" width="10" height="14" rx="1"/><path d="M7.5,7 H12.5 M7.5,10 H12.5 M7.5,13 H10.5"/></svg></span><span class="step__title">Pre-Coaching<br>Questionnaire</span><span class="step__dot"></span><span class="step__text">Lorem ipsum dolor sit amet, con sectetur adipiscing elit, sed do eiusmod temporea.</span></div>
      <div class="step"><span class="icon"><svg viewBox="0 0 20 20"><rect x="3" y="3" width="14" height="8" rx="1"/><circle cx="6" cy="14" r="1.5"/><circle cx="10" cy="14" r="1.5"/><circle cx="14" cy="14" r="1.5"/><path d="M6,7 H14"/></svg></span><span class="step__title">1:1 Coaching<br>Session</span><span class="step__dot"></span><span class="step__text">Lorem ipsum dolor sit amet, con sectetur adipiscing elit, sed do eiusmod temporea.</span></div>
    </div>
  </section>

  <section class="benefits" style="height:248px">
    <h2 class="title title--light" style="position:absolute;left:48px;top:31px;text-align:left">Benefits of Life Coaching<br>Include</h2>
    <ul class="benefits__list" style="top:80px">
      <li>Accountability and support to help you succeed</li><li>Overcome obstacles</li><li>Gain clarity about what you want</li><li>Thrive from your God-given purpose</li><li>Happiness from pursuing and reaching goals</li><li>Encouragement and guidance to help you stay on track</li><li>Strategies to help you reach goals faster</li><li>Energy from doing what excites</li><li>Joy from doing what you love</li><li>Increase productivity</li>
    </ul>
    <div class="round-photo" style="left:287px;top:30px;width:190px;height:190px;background:linear-gradient(100deg,#6a3a18 0%,#b8763a 35%,#e7c79d 65%,#f2e6d8 100%)" role="img" aria-label="Woman with curly hair, eyes closed, hands pressed together in thought"></div>
  </section>

  <section style="height:284px">
    <div class="ring" style="left:48px;top:47px"><div class="ring__photo" role="img" aria-label="Portrait of the coach smiling, wearing glasses" style="background:linear-gradient(160deg,#f1f3f5 0%,#d9dce0 55%,#8a8f96 100%)"></div></div>
    <div class="me__copy" style="top:68px">
      <h2 class="title title--left">About Me</h2>
      <p class="para">Hi. I am Dana Whitfield. I'm a life and career coach. I'm so excited that you are here, ready to take control of your destiny. Like you, I've experienced my share of life's ups, downs, twists, and turns. To overcome those challenges, I remained committed, resilient, and optimistic about my goals and lifelong learning. Most importantly, I couldn't give up because too much was at stake. I had to keep going. So, I am asking you, are you ready to move forward to live beyond your wildest dreams? If so, I invite you to contact me today to learn more.</p>
      <p class="me__line">Let's partner together and co-create your desired future</p>
      <p class="me__sign">Cheers! Dana</p>
    </div>
  </section>

  <section class="quotes" style="height:162px">
    <h2 class="title" style="position:absolute;left:0;right:0;top:21px">Inspirational Quotes</h2>
    <div class="avatar" style="top:70px;background:linear-gradient(160deg,#d9d4cc,#8d7460)" role="img" aria-label="Small round author portrait"><span class="avatar__badge"></span></div>
    <span class="arrow arrow--ghost" style="left:48px;top:97px"><svg viewBox="0 0 6 6"><path d="M4,0.5 L1.5,3 L4,5.5" fill="none" stroke="#fff" stroke-width="1"/></svg></span>
    <span class="arrow arrow--ghost" style="left:462px;top:97px"><svg viewBox="0 0 6 6"><path d="M2,0.5 L4.5,3 L2,5.5" fill="none" stroke="#fff" stroke-width="1"/></svg></span>
    <p class="quote__text" style="top:115px">Lorem ipsum dolor sit amet, consectetur adipiscing elit, sed do eiusmod te</p>
    <p class="quote__by" style="top:130px">Lena Marsh</p>
  </section>

  <section style="height:249px">
    <h2 class="title" style="position:absolute;left:0;right:0;top:39px">Get Started Today</h2>
    <p class="start__text" style="top:80px">Request a free 15-minute phone consultation to see how we can help you achieve your goals. Step boldly into your greatness.<br>Contact us today to start living a happier, more fulfilled, meaningful life.</p>
    <div class="form" style="top:117px">
      <div class="form__row"><div class="field">Name</div><div class="field">Email</div></div>
      <div class="field field--area">Comments</div>
      <span class="btn form__submit">Submit</span>
    </div>
  </section>

  <footer class="site-footer" style="height:164px">
    <div class="footer__body" style="top:0;padding-top:35px">
      <div class="footer__brand"><span class="brand__name">BRIGHTPATH</span><span class="brand__sub">COACHING</span></div>
      <div class="footer__nav"><span>Home</span><i>|</i><span>Coaching Services</span><i>|</i><span>About Us</span><i>|</i><span>Courses</span><i>|</i><span>Contact Us</span></div>
      <div class="footer__contact"><span><svg viewBox="0 0 10 10"><path d="M2,1 L4,1 L5,3.5 L3.8,4.5 C4.5,6 5,6.5 6,6.8 L7,5.5 L9,6.5 L9,8.5 C5,9 1,5 2,1 Z"/></svg>555-014-2290</span><span>|</span><span><svg viewBox="0 0 10 10"><path d="M5,0.5 C7.5,0.5 8.5,2.5 8,4.5 L5,9.5 L2,4.5 C1.5,2.5 2.5,0.5 5,0.5 Z"/></svg>Located in Fairview, NC</span></div>
      <div class="footer__contact" style="margin-top:4px"><span><svg viewBox="0 0 10 10"><rect x="0.5" y="2" width="9" height="6"/></svg>hello@brightpathcoaching.com</span></div>
      <div class="footer__social"><span></span><span></span><span></span><span></span></div>
      <div class="footer__rule"></div>
      <p class="footer__copy">© 2023 <b>BRIGHTPATH COACHING</b> &nbsp;|&nbsp; All Rights Reserved</p>
    </div>
  </footer>
</div>

</body>
</html>
```